SHIELD THE BUSINESS

I'm virtually ready to launch my site, but I have a number of edits and modifications that need to be implemented. More importantly, I'm always looking to improve my site, particularly now that I am making my proverbial "FIRST IMPRESSION." Thus, I'm willing to see if there is someone who can add creativity and perhaps improve what I already have, particularly on the All Important Front Page.

Need extra days to review

```html
<!DOCTYPE html>
<html lang="en">
<head>
<meta charset="utf-8">
<title>Shield The Business – Affordable Legal Service Plan</title>
<link href="https://fonts.googleapis.com/css2?family=Poppins:wght@400;500;600;700&display=swap" rel="stylesheet">
<style>
:root{
  --navy:#0b2157;
  --navy-deep:#081a47;
  --red:#ac0d18;
  --blue:#0e3b8e;
  --ink:#1c1c2e;
  --text:#4a4a5a;
  --pale:#f1f5fc;
  --white:#ffffff;
}
*{margin:0;padding:0;box-sizing:border-box}
html,body{width:1200px;height:4702px;overflow:hidden}
body{position:relative;font-family:'Poppins',sans-serif;color:var(--ink);background:var(--white)}
.abs{position:absolute}
a{color:inherit;text-decoration:none}

/* nav */
.site-nav{position:absolute;left:0;top:0;width:1200px;height:113px;background:var(--white);z-index:3}
.nav-link{position:absolute;top:50px;font-size:14px;color:var(--navy);letter-spacing:.3px}
.nav-link.active{border-bottom:3px solid var(--navy);padding-bottom:18px}
.brand-badge{position:absolute;left:532px;top:18px;width:136px;height:136px;border-radius:50%;background:var(--navy);border:6px solid var(--white);box-shadow:0 0 0 3px var(--red);display:flex;align-items:center;justify-content:center;text-align:center;color:var(--white);font-weight:600;font-size:14px;line-height:1.2;z-index:4}

/* hero */
.hero-media{position:absolute;left:0;top:113px;width:1200px;height:813px;background:radial-gradient(circle at 50% 35%,#4fb8b4 0%,#1f5a62 30%,#1b3437 60%,#0f1e22 100%)}
.hero-box{position:absolute;left:170px;top:694px;width:860px;height:398px;background:var(--navy);border:6px solid var(--white);outline:1px solid #d9dde6;text-align:center;color:var(--white);z-index:2}
.hero-text{margin:48px auto 0;width:720px;font-size:19px;font-weight:600;line-height:41px}
.hero-text strong{font-size:32px;font-weight:600}
.btn{position:absolute;display:flex;align-items:center;justify-content:center;color:var(--white);font-size:19px}
.btn-blue{background:var(--blue)}
.btn-red{background:var(--red)}

/* section heads */
.kicker{position:absolute;width:1200px;text-align:center;font-size:22px;color:var(--ink)}
.section-title{position:absolute;width:1200px;text-align:center;font-weight:600;color:var(--red)}

/* services */
.services-intro{position:absolute;left:200px;top:1298px;width:800px;text-align:center;font-size:15px;line-height:27px;color:var(--text)}
.service-card{position:absolute;width:319px;height:334px;background:var(--white);box-shadow:0 4px 14px rgba(0,0,0,.12)}
.service-media{position:absolute;left:0;top:0;width:319px;height:216px}
.service-icon{position:absolute;left:121px;top:178px;width:77px;height:77px;border-radius:50%;background:var(--red);border:4px solid var(--white);box-shadow:0 0 0 2px #e3b3b6;display:flex;align-items:center;justify-content:center}
.service-name{position:absolute;left:0;width:319px;top:280px;text-align:center;font-size:14px;font-weight:500;color:var(--navy);letter-spacing:.3px}
.service-card.featured{background:var(--navy);color:var(--white);text-align:center}
.featured .service-icon{top:30px}
.featured .service-name{top:126px;color:var(--white)}
.featured .rule{position:absolute;left:136px;top:158px;width:48px;height:2px;background:var(--white)}
.featured p{position:absolute;left:18px;top:178px;width:283px;font-size:12.5px;line-height:21px}
.featured .mini-btn{position:absolute;left:124px;top:272px;width:72px;height:24px;background:var(--red);font-size:9px;line-height:24px}

/* about */
.about-band{position:absolute;left:0;top:2201px;width:1200px;height:670px;background:var(--pale)}
.frame-red{position:absolute;border:2px solid var(--red)}
.about-copy{position:absolute;left:603px;top:2382px;width:493px;font-size:14px;line-height:31px;color:var(--text);text-align:justify}
.about-copy p+p{margin-top:31px}
.btn-navy{background:var(--navy);font-size:14px}

/* cta */
.cta-band{position:absolute;left:0;top:2871px;width:1200px;height:541px;background:var(--navy)}
.cta-line{position:absolute;left:478px;color:var(--white);font-size:39px;line-height:46px}
.cta-strong{position:absolute;left:478px;top:3088px;color:var(--white);font-size:58px;font-weight:600}

/* faq */
.faq-item{position:absolute;left:86px;width:544px;border-bottom:1px solid #d8dbe2}
.faq-q{position:absolute;left:14px;font-size:20px;font-weight:600;color:var(--navy);line-height:26px}
.faq-q b{color:var(--red);font-weight:600;margin-right:8px}
.faq-toggle{position:absolute;left:660px;font-size:26px;color:var(--red);line-height:1}
.faq-a{position:absolute;left:100px;top:3697px;width:496px;font-size:15.5px;line-height:26px;color:var(--text);text-align:justify}

/* footer */
.site-footer{position:absolute;left:0;top:4267px;width:1200px;height:380px;background:var(--navy);color:var(--white)}
.footer-badge{position:absolute;left:88px;top:4351px;width:164px;height:164px;border-radius:50%;border:5px solid var(--white);box-shadow:0 0 0 3px var(--red);background:var(--navy);display:flex;align-items:center;justify-content:center;text-align:center;color:var(--white);font-weight:600;font-size:18px;line-height:1.2}
.social{position:absolute;top:4539px;width:32px;height:32px;background:var(--red);border:2px solid var(--white)}
.foot-head{position:absolute;font-size:21px;font-weight:500}
.foot-head::after{content:"";position:absolute;left:0;bottom:-8px;width:44px;height:2px;background:var(--red)}
.quick-links{position:absolute;left:327px;top:4426px;list-style:none;font-size:15px}
.quick-links li{height:31px}
.quick-links li::before{content:"✶";margin-right:12px;font-size:12px}
.contact-row{position:absolute;left:522px;display:flex;gap:20px;font-size:14px;line-height:18px}
.contact-icon{width:32px;height:32px;background:var(--red);border:2px solid var(--white);border-radius:4px;flex:none;display:flex;align-items:center;justify-content:center}
.news-text{position:absolute;left:866px;top:4426px;width:250px;font-size:14px;line-height:20px}
.news-input{position:absolute;left:866px;top:4488px;width:248px;height:36px;background:var(--white)}
.news-btn{position:absolute;left:866px;top:4537px;width:124px;height:38px;background:var(--red);font-size:13px;display:flex;align-items:center;justify-content:center}
.legal-bar{position:absolute;left:0;top:4647px;width:1200px;height:55px;background:var(--red);color:var(--white);font-size:13px}
.legal-bar span{position:absolute;top:20px}
</style>
</head>
<body>

<header class="site-nav">
  <a class="nav-link active" style="left:86px">HOME</a>
  <a class="nav-link" style="left:166px">ABOUT</a>
  <a class="nav-link" style="left:254px">SERVICES ▾</a>
  <a class="nav-link" style="left:950px">FAQ</a>
  <a class="nav-link" style="left:1017px">CONTACT US</a>
</header>
<div class="brand-badge">Shield<br>The<br>Business</div>

<section class="hero">
  <div class="hero-media" role="img" aria-label="Hand touching a glowing scales-of-justice icon on a digital circuit background"></div>
  <div class="hero-box">
    <p class="hero-text"><strong>BUSINESS OWNERS:</strong> Shield The Business (STB) Is An Extremely Affordable Legal Service Plan (As Little As $8.00 Per Month) That INSULATES Business Owners From Unwarranted LEGAL CLAIMS And Expensive LAWSUITS.</p>
    <a class="btn btn-blue" style="left:124px;top:255px;width:195px;height:70px">LEARN MORE</a>
    <a class="btn btn-red" style="left:334px;top:255px;width:390px;height:70px">SCHEDULE FREE CONSULATION</a>
  </div>
</section>

<section class="services">
  <div class="kicker" style="top:1190px">What We Do</div>
  <h2 class="section-title" style="top:1214px;font-size:51px">OUR SERVICES</h2>
  <p class="services-intro">The price for a membership is a ridiculously low $9.95 PER WEEK. We believe that this fee is very affordable. So what is it? Membership includes the following:</p>

  <div class="service-card" style="left:88px;top:1399px">
    <div class="service-media" role="img" aria-label="Lawyer at a desk with gavel and scales" style="background:linear-gradient(135deg,#d9d2c6,#7d6a55)"></div>
    <div class="service-icon"><svg width="34" height="34" viewBox="0 0 24 24" fill="none" stroke="#fff" stroke-width="1.6"><circle cx="12" cy="7" r="3"/><path d="M5 20v-3a7 4 0 0 1 14 0v3z"/></svg></div>
    <div class="service-name">FREE INITIAL CONSULTATION</div>
  </div>

  <div class="service-card featured" style="left:442px;top:1399px">
    <div class="service-icon"><svg width="34" height="34" viewBox="0 0 24 24" fill="none" stroke="#fff" stroke-width="1.6"><path d="M6 3h9l4 4v14H6z"/><path d="M9 11h7M9 15h7"/></svg></div>
    <div class="service-name">PROPRIETARY CONTRACT LANGUAGE</div>
    <div class="rule"></div>
    <p>STB members are entitled to incorporate exclusive proprietary contract language in their contracts, work orders, and other written agreements</p>
    <div class="mini-btn">LEARN MORE</div>
  </div>

  <div class="service-card" style="left:795px;top:1399px">
    <div class="service-media" role="img" aria-label="Businessman pointing at a free consultation screen" style="background:linear-gradient(135deg,#3e4a5f,#1d2433)"></div>
    <div class="service-icon"><svg width="34" height="34" viewBox="0 0 24 24" fill="none" stroke="#fff" stroke-width="1.6"><circle cx="7" cy="8" r="2.5"/><circle cx="17" cy="8" r="2.5"/><path d="M3 18a4 4 0 0 1 8 0M13 18a4 4 0 0 1 8 0"/></svg></div>
    <div class="service-name">FREE CONSULTATION</div>
  </div>

  <div class="service-card" style="left:88px;top:1753px">
    <div class="service-media" role="img" aria-label="Worried businessman reading a letter" style="background:linear-gradient(135deg,#c8c5c0,#6e5f52)"></div>
    <div class="service-icon"><svg width="34" height="34" viewBox="0 0 24 24" fill="none" stroke="#fff" stroke-width="1.6"><rect x="3" y="6" width="18" height="12"/><path d="M3 6l9 7 9-7"/></svg></div>
    <div class="service-name">FREE ATTORNEY LETTERS</div>
  </div>

  <div class="service-card" style="left:442px;top:1753px">
    <div class="service-media" role="img" aria-label="Judge's gavel resting on banknotes" style="background:linear-gradient(135deg,#cfd3c4,#7a6048)"></div>
    <div class="service-icon"><svg width="34" height="34" viewBox="0 0 24 24" fill="none" stroke="#fff" stroke-width="1.6"><circle cx="12" cy="12" r="8"/><path d="M12 7v10M9.5 9.5h4a1.5 1.5 0 0 1 0 3h-3a1.5 1.5 0 0 0 0 3h4"/></svg></div>
    <div class="service-name">LITIGATION DISCOUNTS</div>
  </div>

  <div class="service-card" style="left:795px;top:1753px">
    <div class="service-media" role="img" aria-label="Lawyer at a desk with gavel and scales" style="background:linear-gradient(135deg,#d9d2c6,#7d6a55)"></div>
    <div class="service-icon"><svg width="34" height="34" viewBox="0 0 24 24" fill="none" stroke="#fff" stroke-width="1.6"><path d="M6 3h9l4 4v14H6z"/><path d="M9 11h7M9 15h5"/></svg></div>
    <div class="service-name">COLLECTIONS</div>
  </div>
</section>

<section>
  <div class="about-band"></div>
  <div class="frame-red" style="left:88px;top:2292px;width:420px;height:466px"></div>
  <div class="abs" role="img" aria-label="Banknote portrait wearing a face mask" style="left:110px;top:2310px;width:420px;height:468px;background:linear-gradient(135deg,#d7dccf,#8d9487 60%,#5d6a5c)"></div>
  <div class="abs" style="left:603px;top:2292px;font-size:22px">Who We Are</div>
  <h2 class="abs" style="left:600px;top:2322px;font-size:43px;font-weight:600;color:var(--red)">ABOUT US</h2>
  <div class="about-copy">
    <p>STB is a group of attorney and legal assistants with many years of experience in litigation, who are devoted to PREVENTING LEGAL CLAIMS and COSTLY LAWSUITS through a variety of FREE and VERY AFFORDABLE services described below.<br>OUR UNIQUE SERVICE PLAN MAKES IT POSSIBLE FOR US TO SHIELD THE BUSINESS.</p>
    <p>A homebuilding company was sued by a former employee who claimed to have been promised a more favorable sales area, which claim was disputed by the homebuilder.</p>
  </div>
  <a class="btn btn-navy" style="left:604px;top:2721px;width:143px;height:50px">READ MORE</a>
</section>

<section>
  <div class="cta-band"></div>
  <svg class="abs" style="left:0;top:2871px" width="484" height="541" viewBox="0 0 484 541" role="img" aria-label="Scales of justice silhouette in a shaft of light">
    <defs><linearGradient id="beam" x1="0" y1="0" x2="1" y2="1"><stop offset="0" stop-color="#7fa3d8"/><stop offset="1" stop-color="#3f5fa0"/></linearGradient></defs>
    <polygon points="0,0 300,0 484,541 0,541" fill="url(#beam)"/>
    <polygon points="0,0 170,0 300,541 0,541" fill="#5578b8" opacity=".6"/>
  </svg>
  <div class="cta-line" style="top:2988px">Contact us to find out how</div>
  <div class="cta-line" style="top:3034px">you can join us to</div>
  <div class="cta-strong">SHIELD THE BUSINESS!!</div>
  <a class="btn btn-red" style="left:482px;top:3205px;width:380px;height:74px;font-size:20px;font-weight:500">SCHEDULE FREE CONSULATION</a>
</section>

<section>
  <div class="kicker" style="top:3512px">FAQs</div>
  <h2 class="section-title" style="top:3545px;font-size:45px">FREQUENTLY ASKED QUESTIONS</h2>

  <div class="faq-item" style="top:3650px;height:149px"></div>
  <div class="faq-q" style="left:100px;top:3656px"><b>01</b>Why should I be concerned about legal claims?</div>
  <div class="faq-toggle" style="top:3654px">–</div>
  <p class="faq-a">Lorem ipsum dolor sit amet, consectetur adipiscing elit. Sus pendisse varius enim in eros elementum tristique. Duis cursus, mi quis viverra ornare, eros dolor interdum nulla, ut commodo diam</p>

  <div class="faq-item" style="top:3799px;height:102px"></div>
  <div class="faq-q" style="left:100px;top:3828px;width:500px"><b>02</b>Provide more details about the value of STB's<br><span style="margin-left:36px">contract language.</span></div>
  <div class="faq-toggle" style="top:3828px">+</div>

  <div class="faq-item" style="top:3901px;height:125px"></div>
  <div class="faq-q" style="left:100px;top:3924px"><b>03</b>If I'm a contractor, for example, how can an STB<br><span style="margin-left:36px">membership minimize legal claims against</span><br><span style="margin-left:36px">my business?</span></div>
  <div class="faq-toggle" style="top:3924px">+</div>

  <div class="faq-item" style="top:4026px;height:78px"></div>
  <div class="faq-q" style="left:100px;top:4051px"><b>04</b>What does an STB membership cost?</div>
  <div class="faq-toggle" style="top:4051px">+</div>

  <div class="faq-item" style="top:4104px;height:75px"></div>
  <div class="faq-q" style="left:100px;top:4126px"><b>05</b>Do you have a Referral Program?</div>
  <div class="faq-toggle" style="top:4126px">+</div>

  <div class="frame-red" style="left:752px;top:3677px;width:384px;height:465px"></div>
  <div class="abs" role="img" aria-label="Attorney in a suit standing in a law library" style="left:732px;top:3697px;width:384px;height:467px;background:linear-gradient(180deg,#6b5545,#3a2e27 55%,#1e1a18)"></div>
</section>

<footer>
  <div class="site-footer"></div>
  <div class="footer-badge">Shield<br>The<br>Business</div>
  <span class="social" style="left:92px"></span>
  <span class="social" style="left:132px"></span>
  <span class="social" style="left:172px"></span>
  <span class="social" style="left:212px"></span>

  <div class="foot-head" style="left:327px;top:4342px">Quick Links</div>
  <ul class="quick-links" style="color:var(--white)">
    <li>Home</li><li>About</li><li>Services</li><li>FAQ</li><li>Contact Us</li>
  </ul>

  <div class="foot-head" style="left:522px;top:4342px">Contact Us</div>
  <div class="contact-row" style="top:4428px;color:var(--white)">
    <span class="contact-icon"><svg width="16" height="16" viewBox="0 0 24 24" fill="#fff"><path d="M6.6 10.8a15 15 0 0 0 6.6 6.6l2.2-2.2a1 1 0 0 1 1-.25 11 11 0 0 0 3.6.6 1 1 0 0 1 1 1V20a1 1 0 0 1-1 1A17 17 0 0 1 3 4a1 1 0 0 1 1-1h3.5a1 1 0 0 1 1 1 11 11 0 0 0 .6 3.6 1 1 0 0 1-.25 1z"/></svg></span>
    <span>CALL US<br>(555) 210-4830 / (800) 555-0147</span>
  </div>
  <div class="contact-row" style="top:4484px;color:var(--white)">
    <span class="contact-icon"><svg width="16" height="16" viewBox="0 0 24 24" fill="none" stroke="#fff" stroke-width="2"><circle cx="12" cy="12" r="9"/><path d="M3 12h18M12 3c3 3.5 3 14.5 0 18M12 3c-3 3.5-3 14.5 0 18"/></svg></span>
    <span>WEBSITE<br>WWW.SHIELDTHEBUSINESS.COM</span>
  </div>
  <div class="contact-row" style="top:4541px;color:var(--white)">
    <span class="contact-icon"><svg width="16" height="16" viewBox="0 0 24 24" fill="#fff"><path d="M12 2a7 7 0 0 0-7 7c0 5 7 13 7 13s7-8 7-13a7 7 0 0 0-7-7zm0 9.5A2.5 2.5 0 1 1 12 6.5a2.5 2.5 0 0 1 0 5z"/></svg></span>
    <span>2400 CANYON RIDGE BLVD.,<br>SUITE 120, SUNVALE, ARIZONA<br>85099</span>
  </div>

  <div class="foot-head" style="left:866px;top:4340px">Our Newsletter</div>
  <p class="news-text">Subscribe our newsletter to get the latest news.</p>
  <div class="news-input"></div>
  <div class="news-btn" style="color:var(--white)">SUBSCRIBE</div>

  <div class="legal-bar">
    <span style="left:86px">Copyright© 2023 SHIELDTHEBUSINESS.NET | All Rights Reserved</span>
    <span style="left:876px">TERMS OF SERVICE | PRIVACY POLICY</span>
  </div>
</footer>

</body>
</html>
```